Private label Bottled water label design

We are launching private label water bottle case packs with our brand “brightway”
Need bottle labels design as well as case pack design artwork. Bottle is 16.9oz similar to pet calvora feltmoor bottles.
It will be spring water.
Case pack will be of 24 bottles
Brightway is a chain of convenience stores in Texas
www.brightwaymarkets.example
I have attached pictures of calvora water. It would be similar packaging for single and case pack.

Target Market(s)

Male female shoppers middle aged. Take home package or single serve in cold vault

Industry/Entity Type

Water bottle retail

Colors
0054AA
0677BA
7BADD7
CADEEF
E8F1F8
59FF00
82FF00
B8FF75
E3FFCB
F4FFEA

Requirements
Must have
• Very premium look. Use the logo of brightway
Nice to have
• Elegant premium water look
Should not have
• I am open to all

```html
<!DOCTYPE html>
<html lang="en">
<head>
<meta charset="utf-8">
<title>Brightway Premium Water – Bottle Label</title>
<link rel="stylesheet" href="https://fonts.googleapis.com/css2?family=Poppins:wght@600;800&display=swap">
<style>
  :root {
    --stage-bg: #e4e4e4;
    --blue-deep: #0677ba;
    --teal: #2f9a8e;
    --green-mid: #4aa866;
    --green-bright: #7bc242;
    --glow: #ffffff;
    --ribbon: #8cc63f;
    --ribbon-edge: #6fae2a;
    --ink: #10202a;
    --ice-light: #d8ecf8;
    --ice-mid: #8cc3e6;
  }
  * { margin: 0; padding: 0; box-sizing: border-box; }
  html, body {
    width: 1200px;
    height: 1086px;
    overflow: hidden;
    background: var(--stage-bg);
  }
  .canvas {
    position: relative;
    width: 1200px;
    height: 1086px;
    display: flex;
    align-items: center;
    justify-content: center;
  }
  .label {
    position: relative;
    width: 1200px;
    height: 230px;
    overflow: hidden;
    background: linear-gradient(20deg, var(--blue-deep) 0%, var(--teal) 40%, var(--green-mid) 65%, var(--green-bright) 100%);
  }
  .label__glow {
    position: absolute;
    left: 50%;
    top: 110px;
    width: 380px;
    height: 300px;
    transform: translate(-50%, -50%);
    background: radial-gradient(ellipse at center, var(--glow) 0%, rgba(255,255,255,0.9) 25%, rgba(255,255,255,0.35) 50%, rgba(255,255,255,0) 72%);
  }
  .label__ice {
    position: absolute;
    left: 0;
    bottom: 0;
    width: 100%;
    height: 92px;
    background: linear-gradient(180deg, rgba(216,236,248,0) 0%, rgba(140,195,230,0.75) 35%, var(--ice-light) 100%);
  }
  .label__brand {
    position: absolute;
    left: 50%;
    top: 60px;
    transform: translateX(-50%);
    display: flex;
    flex-direction: column;
    align-items: center;
  }
  .brand-name {
    display: flex;
    align-items: center;
    gap: 8px;
    font-family: "Poppins", sans-serif;
    font-weight: 800;
    font-size: 38px;
    line-height: 1;
    letter-spacing: -1px;
    color: var(--ink);
  }
  .brand-name__dot {
    width: 14px;
    height: 14px;
    border-radius: 50%;
    background: var(--ribbon-edge);
  }
  .ribbon {
    margin-top: 8px;
    position: relative;
    width: 140px;
    height: 22px;
  }
  .ribbon svg { position: absolute; inset: 0; }
  .ribbon__text {
    position: relative;
    display: block;
    text-align: center;
    font-family: "Poppins", sans-serif;
    font-weight: 600;
    font-size: 11px;
    line-height: 22px;
    letter-spacing: 1px;
    color: #ffffff;
  }
  .volume {
    margin-top: 4px;
    font-family: "Poppins", sans-serif;
    font-weight: 600;
    font-size: 10px;
    letter-spacing: 1px;
    color: var(--ink);
  }
</style>
</head>
<body>
  <main class="canvas">
    <section class="label">
      <div class="label__glow"></div>
      <div class="label__ice" role="img" aria-label="Row of clear ice cubes along the bottom edge of the label"></div>
      <div class="label__brand">
        <div class="brand-name"><span class="brand-name__dot"></span>brightway</div>
        <div class="ribbon">
          <svg width="140" height="22" viewBox="0 0 140 22" aria-hidden="true">
            <polygon points="0,0 140,0 133,11 140,22 0,22 7,11" fill="var(--ribbon)"/>
          </svg>
          <span class="ribbon__text">PREMIUM WATER</span>
        </div>
        <div class="volume">16.9OZ</div>
      </div>
    </section>
  </main>
</body>
</html>
```